Desk Allies Business Card

Contact Information for Business Card

Janne Voutilainen
Managing Director

3/47 Brindle Street Mitchell ACT 2911

Tel: +61 02 6257 3140
Mob: +61 0427 315 846

Email: janne@deskallies.com.au
Web: www.deskallies.com.au

Colors

Designer to choose colors to be used in the design.

Requirements
Must have
• Logo, Name, Title, Address, Telephone, Mobile, Email Address and Website
• "Desk Ally International Pty Ltd"

```html
<!DOCTYPE html>
<html lang="en">
<head>
<meta charset="utf-8">
<title>Desk Allies Business Card</title>
<link rel="stylesheet" href="https://fonts.googleapis.com/css2?family=Lato:wght@300;400;700;900&display=swap">
<style>
  :root {
    --backdrop: #242424;
    --brand-blue: #2286ca;
    --brand-blue-soft: rgba(255,255,255,0.28);
    --card-white: #ffffff;
    --ink: #2b2b2b;
    --ink-muted: #555555;
    --rule: #3a3a3a;
  }
  * { box-sizing: border-box; margin: 0; padding: 0; }
  html, body { width: 1200px; height: 1200px; overflow: hidden; }
  body {
    background: var(--backdrop);
    font-family: "Lato", Arial, sans-serif;
    display: flex;
    align-items: center;
    justify-content: center;
    gap: 60px;
  }
  .card {
    position: relative;
    width: 480px;
    height: 780px;
    border-radius: 24px;
    overflow: hidden;
  }

  /* Front face */
  .card--front { background: var(--card-white); color: var(--ink); }
  .card__band { position: absolute; left: 0; width: 480px; height: 60px; }
  .card__band--top { top: 0; }
  .card__band--bottom { bottom: 0; }
  .brand {
    position: absolute; top: 105px; left: 0; right: 0;
    text-align: center;
  }
  .brand__dot {
    width: 70px; height: 70px; margin: 0 auto 20px;
    border-radius: 50%; border: 12px solid var(--brand-blue);
  }
  .brand__name {
    font-weight: 700; font-size: 40px; color: var(--brand-blue);
    letter-spacing: 0.5px; text-transform: uppercase; line-height: 1;
  }
  .brand__tagline {
    margin-top: 6px; font-size: 14px; letter-spacing: 3px;
    color: var(--ink-muted); text-transform: uppercase;
  }
  .person {
    position: absolute; top: 360px; left: 0; right: 0; text-align: center;
  }
  .person__name {
    font-weight: 900; font-size: 38px; text-transform: uppercase; color: var(--ink);
    letter-spacing: 0.3px;
  }
  .person__title { font-weight: 300; font-size: 26px; color: var(--ink-muted); margin-top: 2px; }
  .contact {
    position: absolute; top: 530px; left: 0; right: 0;
    font-size: 19px; line-height: 1.45; text-align: center;
  }
  .contact__label { color: var(--brand-blue); font-weight: 700; }
  .contact__rule {
    width: 320px; height: 1px; background: var(--rule); margin: 14px auto 12px;
  }
  .address { font-size: 19px; line-height: 1.3; text-align: center; color: var(--ink); }

  /* Back face */
  .card--back { background: var(--brand-blue); color: #fff; }
  .back__ring {
    position: absolute; top: 150px; left: 110px;
    width: 260px; height: 260px; border-radius: 50%;
    border: 34px solid var(--brand-blue-soft);
  }
  .back__brand { position: absolute; top: 540px; left: 0; right: 0; text-align: center; }
  .back__name { font-size: 44px; font-weight: 400; text-transform: uppercase; line-height: 1; }
  .back__tagline { font-size: 21px; text-transform: uppercase; margin-top: 8px; letter-spacing: 0.3px; }
  .back__rule { width: 390px; height: 1px; background: rgba(255,255,255,0.7); margin: 60px auto 20px; }
  .back__company { font-size: 18px; text-transform: uppercase; }
</style>
</head>
<body>
  <section class="card card--front">
    <svg class="card__band card__band--top" viewBox="0 0 480 60" aria-hidden="true">
      <polygon points="0,0 480,0 480,5 445,55 65,55 30,5 0,5" fill="var(--brand-blue)"/>
    </svg>
    <div class="brand">
      <div class="brand__dot"></div>
      <div class="brand__name">Desk Allies</div>
      <div class="brand__tagline">Ergonomic Office Environments</div>
    </div>
    <div class="person">
      <h1 class="person__name">Janne Voutilainen</h1>
      <p class="person__title">Managing Director</p>
    </div>
    <div class="contact">
      <p><span class="contact__label">Tel:</span> +61 02 6257 3140</p>
      <p><span class="contact__label">Mob:</span> +61 0427 315 846</p>
      <p><span class="contact__label">Email:</span> janne@deskallies.com.au</p>
      <p><span class="contact__label">Web:</span> www.deskallies.com.au</p>
      <div class="contact__rule"></div>
      <p class="address">3/47 Brindle Street Mitchell<br>ACT 2911</p>
    </div>
    <svg class="card__band card__band--bottom" viewBox="0 0 480 60" aria-hidden="true">
      <polygon points="0,60 480,60 480,55 445,5 65,5 30,55 0,55" fill="var(--brand-blue)"/>
    </svg>
  </section>

  <section class="card card--back">
    <div class="back__ring" aria-hidden="true"></div>
    <div class="back__brand">
      <div class="back__name">Desk Allies</div>
      <div class="back__tagline">Ergonomic&nbsp; Office Envirnments</div>
      <div class="back__rule"></div>
      <div class="back__company">Desk Ally International Pty Ltd</div>
    </div>
  </section>
</body>
</html>
```